Bamboo & Ember Business Card FUN & EXCITING

Here is the Information for the Card:
Harpreet Kalra (Toby)
E: TobyKalra@mailbox-demo.com
C: (480) 555-0147
www.BambooEmberLV.com

We don't want traditional Indian cliche, We a playful bold and fun business card.

Files: https://files.sharebox-demo.net/folders/7QtpLmzR2xVbN4kHs9wYcDfJ3eGaUoPi

https://files.sharebox-demo.net/folders/5ZrqTwyX8mKcE2vBn6aLpHsQ9uFjRgOe

Target Market(s)

Las Vegas Local Restaurant

Industry/Entity Type

Indian Restaurant

Contact Information for Business Card

Name, Email, Cell Phone, Company Logo

```html
<!DOCTYPE html>
<html lang="en">
<head>
<meta charset="utf-8">
<title>Bamboo &amp; Ember — Business Card</title>
<link rel="stylesheet" href="https://fonts.googleapis.com/css2?family=Libre+Baskerville:wght@400;700&family=Tinos&display=swap">
<style>
  :root {
    --backdrop: #2b2b2d;
    --cream: #f6ecd3;
    --pink: #e2236a;
    --ink: #1c1712;
    --gold: #f2c230;
    --rice: #f3f1ea;
    --dal: #c98a2c;
    --bowl: #4a3426;
    --cloth: #c9c6c0;
    --curry-red: #b5401c;
    --curry-gold: #d08a2e;
    --plate-blue: #a9b7be;
    --marble: #e4e2dd;
    --skillet: #2a2624;
  }
  * { margin: 0; padding: 0; box-sizing: border-box; }
  html, body { width: 1125px; height: 1200px; overflow: hidden; }
  body {
    background: var(--backdrop);
    position: relative;
    font-family: "Tinos", "Times New Roman", serif;
  }
  .card {
    position: absolute;
    left: 150px;
    width: 826px;
    height: 472px;
    overflow: hidden;
    box-shadow: 0 6px 18px rgba(0,0,0,.45);
  }
  .card--front { top: 98px; background: var(--cream); }
  .card--back { top: 630px; }

  /* Front */
  .front__photo {
    position: absolute; inset: 0 0 0 390px;
    background:
      radial-gradient(ellipse 60% 55% at 62% 60%, var(--rice) 0%, rgba(243,241,234,0) 70%),
      radial-gradient(ellipse 75% 70% at 45% 52%, var(--dal) 0%, rgba(201,138,44,0) 75%),
      linear-gradient(160deg, var(--curry-red) 0%, var(--bowl) 35%, var(--cloth) 100%);
  }
  .front__band { position: absolute; inset: 0; width: 100%; height: 100%; }

  .brand-name {
    position: absolute;
    left: 40px; top: 44px;
    width: 340px;
    font-family: "Libre Baskerville", Georgia, serif;
    font-weight: 700;
    font-size: 50px;
    line-height: 1.1;
    color: var(--pink);
    text-transform: uppercase;
  }
  .person-name {
    position: absolute;
    left: 40px; top: 262px;
    font-family: "Libre Baskerville", Georgia, serif;
    font-weight: 700;
    font-size: 29px;
    color: var(--ink);
    text-shadow: 2px 2px 0 var(--gold);
    white-space: nowrap;
  }
  .contact {
    position: absolute;
    left: 40px; top: 326px;
    list-style: none;
    font-size: 27px;
    line-height: 36px;
    color: var(--ink);
  }

  /* Back */
  .back__photo {
    position: absolute; inset: 0;
    background:
      radial-gradient(ellipse 20% 30% at 28% 55%, var(--rice) 0%, rgba(243,241,234,.85) 60%, rgba(243,241,234,0) 100%),
      radial-gradient(ellipse 24% 38% at 28% 58%, var(--skillet) 0%, rgba(42,38,36,0) 100%),
      radial-gradient(ellipse 30% 40% at 62% 60%, var(--curry-gold) 0%, rgba(208,138,46,0) 100%),
      radial-gradient(ellipse 28% 30% at 60% 12%, var(--curry-red) 0%, rgba(181,64,28,0) 100%),
      radial-gradient(ellipse 22% 40% at 96% 70%, #e0b070 0%, rgba(224,176,112,0) 100%),
      radial-gradient(ellipse 22% 30% at 4% 20%, var(--curry-red) 0%, rgba(181,64,28,0) 100%),
      linear-gradient(135deg, var(--plate-blue) 0%, var(--marble) 50%, var(--plate-blue) 100%);
  }
  .back__brand {
    position: absolute;
    left: 132px; top: 196px;
    width: 200px;
    text-align: center;
    font-family: "Libre Baskerville", Georgia, serif;
    font-weight: 700;
    font-size: 28px;
    line-height: 1.15;
    color: var(--ink);
    text-transform: uppercase;
  }
</style>
</head>
<body>
  <section class="card card--front">
    <div class="front__photo" role="img" aria-label="Photo of a bowl of yellow dal beside white basmati rice with herbs, tomatoes and a striped cloth"></div>
    <svg class="front__band" viewBox="0 0 826 472" aria-hidden="true">
      <polygon points="0,0 390,0 455,472 0,472" fill="var(--cream)"/>
      <polygon points="390,0 406,0 471,472 455,472" fill="var(--pink)"/>
    </svg>
    <div class="brand-name">Bamboo &amp; Ember</div>
    <div class="person-name">Harpreet Kalra (Toby)</div>
    <ul class="contact">
      <li>(480) 555-0147</li>
      <li>TobyKalra@mailbox-demo.com</li>
      <li>www.BambooEmberLV.com</li>
    </ul>
  </section>

  <section class="card card--back">
    <div class="back__photo" role="img" aria-label="Overhead photo of an Indian food spread: curries, paneer, rice in a skillet and puffed bread on marble"></div>
    <div class="back__brand">Bamboo &amp; Ember</div>
  </section>
</body>
</html>
```